Dental Business Card Design

Need to have a business card designed around my logo. I would like to have a unique, professional, and, eye catching designs. Can be associated with the colors within the logo, but not required and would actually like to see other color combinations that may work well with the logo. The back of the card is going to be an appointment reminder. I can provide you with the specific information for that needs to be on the back of the card if it's important for the design. i am an Oral Surgeon and the Business name is "Harbor Crest Oral Surgery" The logo does have the name already incorporated into the design, however, if changing the fonts I would like to have the "Oral Surgery" emphasized. Please feel free to contact me with any questions as this is very important. I don't want to have any typical dental "tooth, mirror, etc." on the business card. Thank you.

```html
<!DOCTYPE html>
<html lang="en">
<head>
<meta charset="UTF-8">
<title>Harbor Crest Oral Surgery – Appointment Card</title>
<link rel="stylesheet" href="https://fonts.googleapis.com/css2?family=Arimo:wght@400;700&family=Roboto+Condensed:wght@400;700&display=swap">
<style>
  :root {
    --ink: #111111;
    --paper: #ffffff;
    --navy: #0b3a9f;
    --sky: #2f8ce2;
    --accent-blue: #1a55c6;
    --reminder-yellow: #fff27a;
    --teal: #7ef0dc;
  }
  * { margin: 0; padding: 0; box-sizing: border-box; }
  html, body { width: 1200px; height: 686px; overflow: hidden; background: var(--paper); }
  .card {
    position: relative;
    width: 1200px;
    height: 686px;
    background: var(--paper);
    overflow: hidden;
    font-family: "Roboto Condensed", "Arial Narrow", sans-serif;
    color: var(--ink);
  }
  .panel-art { position: absolute; inset: 0; }
  .label {
    position: absolute;
    font-family: "Arimo", Arial, sans-serif;
    font-size: 32px;
    line-height: 1;
    white-space: nowrap;
  }
  .rule { position: absolute; height: 0; border-top: 2.5px solid var(--ink); }
  .days { position: absolute; left: 51px; top: 329px; display: flex; gap: 0; }
  .day {
    position: absolute;
    top: 0;
    display: flex;
    align-items: center;
    font-size: 35px;
    line-height: 34px;
    white-space: nowrap;
  }
  .day-box {
    width: 34px; height: 34px;
    border: 2.2px solid var(--ink);
    margin-right: 3px;
    flex: none;
  }
  .reminder {
    position: absolute;
    left: 774px;
    top: 58px;
    width: 410px;
    color: var(--paper);
    font-size: 34.5px;
    line-height: 40.5px;
  }
  .reminder-title {
    font-family: "Arimo", Arial, sans-serif;
    font-weight: 700;
    font-size: 32px;
    color: var(--reminder-yellow);
    line-height: 40px;
  }
  .reminder-online {
    margin-top: 16px;
    font-family: "Arimo", Arial, sans-serif;
    font-weight: 700;
    font-size: 32.5px;
    line-height: 44.5px;
  }
  .policy {
    position: absolute;
    left: 51px;
    top: 519px;
    color: var(--accent-blue);
    font-size: 33.5px;
    line-height: 42px;
    white-space: nowrap;
  }
  .policy-title { font-weight: 700; }
</style>
</head>
<body>
<main class="card">
  <svg class="panel-art" width="1200" height="686" viewBox="0 0 1200 686" aria-hidden="true">
    <defs>
      <linearGradient id="panelFill" x1="0" y1="0" x2="1" y2="0">
        <stop offset="0" stop-color="#0a35a0"/>
        <stop offset="0.55" stop-color="#1d63cc"/>
        <stop offset="1" stop-color="#3392e6"/>
      </linearGradient>
      <linearGradient id="swooshFill" x1="0" y1="0" x2="1" y2="0">
        <stop offset="0" stop-color="#4fd8c8"/>
        <stop offset="0.45" stop-color="#8ff3e2"/>
        <stop offset="1" stop-color="#ffffff" stop-opacity="0.2"/>
      </linearGradient>
    </defs>
    <path class="swoosh" fill="url(#swooshFill)"
      d="M684,432 C740,500 840,545 960,530 C1060,515 1140,470 1200,430 L1200,394 C1100,450 990,505 880,510 C800,512 740,480 684,432 Z"/>
    <path class="panel" fill="url(#panelFill)"
      d="M731,0 L1200,0 L1200,394 C1110,445 990,505 880,508 C810,510 765,492 731,474 Z"/>
  </svg>

  <p class="label" style="left:51px; top:85px;">Next Appointment is for:</p>
  <div class="rule" style="left:51px; top:175px; width:643px;"></div>
  <div class="rule" style="left:51px; top:242px; width:643px;"></div>

  <p class="label" style="left:51px; top:287px;">on:</p>

  <div class="days">
    <span class="day" style="left:0;"><span class="day-box"></span>Mon</span>
    <span class="day" style="left:122px;"><span class="day-box"></span>Tue</span>
    <span class="day" style="left:231px;"><span class="day-box"></span>Wed</span>
    <span class="day" style="left:355px;"><span class="day-box"></span>Thu</span>
    <span class="day" style="left:466px;"><span class="day-box"></span>Fri</span>
    <span class="day" style="left:560px;"><span class="day-box"></span>Sat</span>
  </div>

  <p class="label" style="left:51px; top:404px;">Date:</p>
  <div class="rule" style="left:141px; top:429px; width:222px;"></div>
  <p class="label" style="left:366px; top:404px;">Time:</p>
  <div class="rule" style="left:463px; top:429px; width:231px;"></div>

  <section class="reminder">
    <p class="reminder-title">Please remember:</p>
    <p>Nothing to eat or drink<br>6 hours prior to IV Sedation.<br>Bring any necessary x-rays,<br>medications, and referral<br>slips with you.</p>
    <p class="reminder-online">Save time by filling<br>out your Medical<br>history online.</p>
  </section>

  <section class="policy">
    <p class="policy-title">A broken appointment is a loss for everyone.</p>
    <p>Please inform us 24 hours in advance if you are unable to keep your<br>appointment or you may be charged for a missed visit.</p>
  </section>
</main>
</body>
</html>
```